Web Design for Harbor Ledger Allies

Harbor Ledger Allies needs the photoshop files for a simple, clean and professional website design. The company is building a network of bookkeepers/accountants to handle outsourced bookkeeping services for start ups and small businesses. It needs to both attract bookkeepers to become partners and give clients confidence in the professional network. The partners will use products like Tallymint Web, Brightfolio.example and PennyTrim.example for start ups, as well as help with tasks using the clients existing accounting software.

A home and subpage design is needed. I'll award the work based on the home design. The minor subpage changes can be worked out in the workroom stage.

The pages for the navigation will be: Home, Services, Locations, Partners, FAQ, Contact

```html
<!DOCTYPE html>
<html lang="en">
<head>
<meta charset="utf-8">
<title>Harbor Ledger Allies</title>
<link href="https://fonts.googleapis.com/css2?family=Lato:wght@300;400;700&display=swap" rel="stylesheet">
<style>
:root{
  --blue:#1b9ad6;
  --charcoal:#58595b;
  --text:#3a3a3a;
  --muted:#6e6e6e;
  --page:#f2f2f2;
  --white:#ffffff;
  --rule:#dcdcdc;
  --logo-grey:#9a9a9a;
}
*{margin:0;padding:0;box-sizing:border-box}
html,body{width:1040px;height:1200px;overflow:hidden}
body{position:relative;font-family:"Lato",sans-serif;color:var(--text);background:var(--page)}
.abs{position:absolute}

/* hero */
.hero-photo{left:0;top:0;width:1040px;height:460px;
  background:linear-gradient(100deg,#8e97a4 0%,#5c6878 30%,#2a3548 60%,#1c2436 80%,#3b4658 100%)}
.site-header{left:0;top:0;width:1040px;height:76px;background:rgba(255,255,255,.93)}
.brand{left:138px;top:20px;display:flex;align-items:center;gap:10px}
.brand-mark{width:34px;height:34px;border-radius:50%;background:var(--blue)}
.brand-name{font-weight:700;font-size:15px;line-height:15px;color:var(--blue);width:120px;text-transform:uppercase}
.main-nav{left:478px;top:32px;display:flex;gap:23px;font-size:10.5px;color:#555;letter-spacing:.2px}
.nav-divider{left:866px;top:26px;width:1px;height:26px;background:#333}
.search{left:878px;top:24px}
.hero-title{left:0;top:157px;width:1040px;text-align:center;color:#fff;font-weight:300;font-size:36px;letter-spacing:-.3px}
.hero-sub{left:0;top:198px;width:1040px;text-align:center;color:#fff;font-weight:300;font-size:21px;letter-spacing:-.3px}
.cta-label{top:279px;width:225px;text-align:center;font-size:16px;font-weight:700;letter-spacing:.2px}
.cta-label.accountant{left:253px;color:var(--blue)}
.cta-label.client{left:557px;color:#fff}
.cta-btn{top:307px;width:225px;height:45px;display:flex;align-items:center;justify-content:center;color:#fff;font-weight:700;font-size:17px;letter-spacing:.3px}
.cta-btn.register{left:253px;background:var(--blue)}
.cta-btn.signup{left:557px;background:var(--charcoal)}
.or-line{top:329px;width:12px;height:1px;background:#c8c8c8}
.or-badge{left:500px;top:311px;width:36px;height:36px;border-radius:50%;background:#fff;display:flex;align-items:center;justify-content:center;font-size:11px;font-weight:700;color:#333}

/* featured */
.section-title{font-size:19px;font-weight:700;letter-spacing:-.3px;text-transform:uppercase}
.featured-title{left:141px;top:503px;color:var(--blue)}
.card{width:212px;height:171px;background:#fff;border:1px solid #e6e6e6;overflow:hidden}
.card-head{position:absolute;left:0;top:0;width:100%;height:74px;background:var(--charcoal)}
.avatar{position:absolute;left:16px;top:8px;width:77px;height:77px;border:3px solid #fff;background:linear-gradient(160deg,#c9a489,#7b5a48)}
.card-name{position:absolute;left:106px;top:14px;color:#fff;font-size:14px;font-weight:700}
.hire{position:absolute;left:106px;top:37px;width:82px;height:29px;background:var(--blue);color:#fff;font-size:12px;font-weight:700;display:flex;align-items:center;justify-content:center}
.facts{position:absolute;left:17px;top:96px;width:180px;display:grid;grid-template-columns:78px 1fr;grid-auto-rows:18.5px;align-items:center;font-size:10px}
.facts dt{color:var(--muted);white-space:nowrap}
.facts dd{color:#222;white-space:nowrap}
.facts dd.rate{font-size:13.5px}

/* service requests */
.requests{left:619px;top:452px;width:285px;height:450px;background:#fff}
.results{position:absolute;left:29px;top:20px;font-size:10.5px;color:var(--muted)}
.requests .section-title{position:absolute;left:28px;top:51px;color:#555}
.job{position:absolute;left:28px;width:243px}
.job-title{font-size:12.5px;color:var(--blue)}
.job-co{font-size:10px;color:#555;margin-top:3px}
.meta{position:absolute;font-size:10px;color:#444;display:flex;align-items:center;gap:5px;white-space:nowrap}
.job-rule{position:absolute;left:21px;width:243px;height:1px;background:var(--rule)}
.more{position:absolute;left:28px;top:421px;font-size:11px;color:#444;text-decoration:underline;display:flex;align-items:center;gap:9px}

/* partners strip */
.logos{left:0;top:940px;width:1040px;height:78px;background:#fff}
.logo-item{position:absolute;top:30px;font-size:16px;font-weight:400;color:var(--logo-grey);white-space:nowrap}
.partner-band{left:0;top:1018px;width:1040px;height:100px;background:var(--charcoal);color:#fff}
.partner-band h2{position:absolute;left:137px;top:24px;font-size:19px;font-weight:700;letter-spacing:-.5px}
.partner-band p{position:absolute;left:138px;top:58px;font-size:11px;line-height:14px;width:560px}
.band-btn{position:absolute;left:763px;top:44px;width:143px;height:29px;border-radius:15px;background:var(--blue);font-size:12px;font-weight:700;display:flex;align-items:center;justify-content:center}

/* footer */
.site-footer{left:0;top:1118px;width:1040px;height:82px;background:#f4f4f4}
.foot-nav{position:absolute;left:137px;top:32px;font-size:9px;color:#444;letter-spacing:.2px}
.copyright{position:absolute;left:138px;top:52px;font-size:9.5px;color:#888}
.social{position:absolute;left:560px;top:33px;display:flex;gap:10px;font-size:10px;color:#999}
.foot-brand{position:absolute;left:790px;top:30px;display:flex;align-items:center;gap:7px}
.foot-brand .brand-mark{width:20px;height:20px;background:#aaa}
.foot-brand span{font-size:9px;font-weight:700;color:#aaa;width:70px;line-height:9px;text-transform:uppercase}
</style>
</head>
<body>

<div class="abs hero-photo" role="img" aria-label="Photo of business professionals in suits reviewing a tablet at a desk"></div>

<header class="abs site-header"></header>
<div class="abs brand"><span class="brand-mark"></span><span class="brand-name">Harbor Ledger Allies</span></div>
<nav class="abs main-nav"><span>HOME</span><span>SERVICES</span><span>LOCATIONS</span><span>PARTNERS</span><span>FAQ</span><span>CONTACT</span></nav>
<div class="abs nav-divider"></div>
<svg class="abs search" width="28" height="28" viewBox="0 0 28 28" aria-label="Search"><circle cx="11" cy="11" r="8" fill="none" stroke="#222" stroke-width="2.6"/><line x1="17" y1="17" x2="25" y2="25" stroke="#222" stroke-width="3.4" stroke-linecap="round"/></svg>

<h1 class="abs hero-title">ACCOUNTANTS &amp; BOOKKEEPERS</h1>
<p class="abs hero-sub">YOUR PRACTICE. YOUR CLIENTS. ONE PLATFORM</p>

<div class="abs cta-label accountant">REGISTER AS ACCOUNTANT</div>
<div class="abs cta-label client">HIRE AN ACCOUNTANT</div>
<div class="abs cta-btn register">REGISTER NOW!</div>
<div class="abs or-line" style="left:484px"></div>
<div class="abs or-line" style="left:540px"></div>
<div class="abs or-badge">OR</div>
<div class="abs cta-btn signup">SIGN UP NOW!</div>

<h2 class="abs section-title featured-title">Featured Accountants</h2>

<article class="abs card" style="left:138px;top:542px">
  <div class="card-head"></div>
  <div class="avatar" role="img" aria-label="Portrait photo of Owen Harte"></div>
  <div class="card-name">Owen Harte</div><div class="hire">HIRE ME</div>
  <dl class="facts"><dt>Qualification:</dt><dd>CQAB, America</dd><dt>Experience:</dt><dd>10 Years</dd><dt>Hourly Rate:</dt><dd class="rate">$25/Hour</dd></dl>
</article>
<article class="abs card" style="left:369px;top:542px">
  <div class="card-head"></div>
  <div class="avatar" role="img" aria-label="Portrait photo of Mara Quill"></div>
  <div class="card-name">Mara Quill</div><div class="hire">HIRE ME</div>
  <dl class="facts"><dt>Qualification:</dt><dd>CQAB, America</dd><dt>Experience:</dt><dd>10 Years</dd><dt>Hourly Rate:</dt><dd class="rate">$25/Hour</dd></dl>
</article>
<article class="abs card" style="left:138px;top:730px">
  <div class="card-head"></div>
  <div class="avatar" role="img" aria-label="Portrait photo of Delia"></div>
  <div class="card-name">Delia</div><div class="hire">HIRE ME</div>
  <dl class="facts"><dt>Qualification:</dt><dd>CQAB, America</dd><dt>Experience:</dt><dd>10 Years</dd><dt>Hourly Rate:</dt><dd class="rate">$25/Hour</dd></dl>
</article>
<article class="abs card" style="left:369px;top:730px">
  <div class="card-head"></div>
  <div class="avatar" role="img" aria-label="Portrait photo of Tobin Reyes"></div>
  <div class="card-name">Tobin Reyes</div><div class="hire">HIRE ME</div>
  <dl class="facts"><dt>Qualification:</dt><dd>CQAB, America</dd><dt>Experience:</dt><dd>10 Years</dd><dt>Hourly Rate:</dt><dd class="rate">$25/Hour</dd></dl>
</article>

<aside class="abs requests">
  <div class="results">1-15 of 13750 Results</div>
  <h2 class="section-title">Service Requests</h2>

  <div class="job" style="top:91px"><div class="job-title">Staff Accountant - Payroll</div><div class="job-co">Clearwell Care Services</div></div>
  <div class="job" style="top:199px"><div class="job-title">Client Accounting Manager</div><div class="job-co">Varden Holloway &amp; Co., LLC</div></div>
  <div class="job" style="top:312px"><div class="job-title">Audit Senior Manager</div><div class="job-co">Ostrand &amp; Pell</div></div>

  <div class="meta" style="left:28px;top:134px"><svg width="11" height="10" viewBox="0 0 11 10"><rect x="0.5" y="2.5" width="10" height="7" fill="none" stroke="#333"/><rect x="3.5" y="0.5" width="4" height="2" fill="none" stroke="#333"/></svg>Competitive</div>
  <div class="meta" style="left:156px;top:134px"><svg width="8" height="11" viewBox="0 0 8 11"><path d="M4 11 L0.8 5 A3.5 3.5 0 1 1 7.2 5 Z" fill="#333"/><circle cx="4" cy="4" r="1.3" fill="#fff"/></svg>Austin, TX</div>
  <div class="meta" style="left:28px;top:153px"><svg width="11" height="11" viewBox="0 0 11 11"><circle cx="5.5" cy="5.5" r="4.6" fill="none" stroke="#333" stroke-width="1.2"/><path d="M5.5 3 V5.7 H7.5" fill="none" stroke="#333"/></svg>Permanent, Full time</div>
  <div class="meta" style="left:155px;top:153px"><svg width="12" height="11" viewBox="0 0 12 11"><rect x="0.5" y="1.5" width="11" height="9" fill="none" stroke="#333"/><rect x="0.5" y="1.5" width="11" height="2.5" fill="#333"/></svg>Posted on: 02 Jun 14</div>
  <div class="job-rule" style="top:181px"></div>

  <div class="meta" style="left:28px;top:242px"><svg width="11" height="10" viewBox="0 0 11 10"><rect x="0.5" y="2.5" width="10" height="7" fill="none" stroke="#333"/><rect x="3.5" y="0.5" width="4" height="2" fill="none" stroke="#333"/></svg>Competitive</div>
  <div class="meta" style="left:156px;top:242px"><svg width="8" height="11" viewBox="0 0 8 11"><path d="M4 11 L0.8 5 A3.5 3.5 0 1 1 7.2 5 Z" fill="#333"/><circle cx="4" cy="4" r="1.3" fill="#fff"/></svg>Alexandria, LA</div>
  <div class="meta" style="left:28px;top:261px"><svg width="11" height="11" viewBox="0 0 11 11"><circle cx="5.5" cy="5.5" r="4.6" fill="none" stroke="#333" stroke-width="1.2"/><path d="M5.5 3 V5.7 H7.5" fill="none" stroke="#333"/></svg>Permanent, Full time</div>
  <div class="meta" style="left:155px;top:261px"><svg width="12" height="11" viewBox="0 0 12 11"><rect x="0.5" y="1.5" width="11" height="9" fill="none" stroke="#333"/><rect x="0.5" y="1.5" width="11" height="2.5" fill="#333"/></svg>Posted on: 02 Jun 14</div>
  <div class="job-rule" style="top:294px"></div>

  <div class="meta" style="left:28px;top:355px"><svg width="11" height="10" viewBox="0 0 11 10"><rect x="0.5" y="2.5" width="10" height="7" fill="none" stroke="#333"/><rect x="3.5" y="0.5" width="4" height="2" fill="none" stroke="#333"/></svg>Competitive</div>
  <div class="meta" style="left:156px;top:355px"><svg width="8" height="11" viewBox="0 0 8 11"><path d="M4 11 L0.8 5 A3.5 3.5 0 1 1 7.2 5 Z" fill="#333"/><circle cx="4" cy="4" r="1.3" fill="#fff"/></svg>Riverside, CA</div>
  <div class="meta" style="left:28px;top:374px"><svg width="11" height="11" viewBox="0 0 11 11"><circle cx="5.5" cy="5.5" r="4.6" fill="none" stroke="#333" stroke-width="1.2"/><path d="M5.5 3 V5.7 H7.5" fill="none" stroke="#333"/></svg>Permanent, Full time</div>
  <div class="meta" style="left:155px;top:374px"><svg width="12" height="11" viewBox="0 0 12 11"><rect x="0.5" y="1.5" width="11" height="9" fill="none" stroke="#333"/><rect x="0.5" y="1.5" width="11" height="2.5" fill="#333"/></svg>Posted on: 02 Jun 14</div>
  <div class="job-rule" style="top:408px"></div>

  <div class="more">MORE JOBS <svg width="16" height="16" viewBox="0 0 16 16"><circle cx="8" cy="8" r="6.8" fill="none" stroke="#333" stroke-width="1.8"/><path d="M6.5 4.8 L9.6 8 L6.5 11.2" fill="none" stroke="#333" stroke-width="1.8"/></svg></div>
</aside>

<section class="abs logos" aria-label="Partner software">
  <span class="logo-item" style="left:142px">Wintally</span>
  <span class="logo-item" style="left:285px">Plumgrove</span>
  <span class="logo-item" style="left:428px">Zenlo</span>
  <span class="logo-item" style="left:493px;font-size:12px;top:33px">Brightfolio.example</span>
  <span class="logo-item" style="left:630px">skyledger books</span>
  <span class="logo-item" style="left:773px;font-size:14px;top:32px">PennyTrim.example</span>
</section>

<section class="abs partner-band">
  <h2>Partner With Us</h2>
  <p>Partnering with HarborLedger lets your clients get the most from your expertise and experience.<br>Together, we can make small business better.</p>
  <div class="band-btn">SIGN UP FOR FREE</div>
</section>

<footer class="abs site-footer">
  <div class="foot-nav">HOME / &nbsp;SERVICES &nbsp;/ &nbsp;LOCATIONS &nbsp;/ &nbsp;PARTNERS &nbsp;/ &nbsp;FAQ &nbsp;/ &nbsp;CONTACT</div>
  <div class="copyright">Copyright © HARBORLEDGERALLIES. All Right Reserved.</div>
  <div class="social"><span>Pagebook</span><span>Chirper</span><span>Circlez</span><span>Tubely</span></div>
  <div class="foot-brand"><span class="brand-mark"></span><span>Harbor Ledger Allies</span></div>
</footer>

</body>
</html>
```